Quick Tray Packs

Need a very simple diagonal random design on bag. using 2 colors only
Packaging material on a roll. 11' Wide total, do not need eye spot since it is random print.
Target Market(s)
hospitality industry
Colors
Designer to choose colors to be used in the design.
Requirements
Must have
- Open for design ideas very simple since it is repeat.the text should be diagonal.
- Need for whole bag to be black, the test can be in Gold.
- On the front of the bag:
- Velvet Crest Coffee
- 100% Arabica Coffee
- Back of the bag:
- This package contains one filter pack coffee and may
- also contain sugar, non-dairy creamer, sugar sub., and stirrer.
- Corvane & Reed Coffee
- Brenhollow, TX 75811

```html
<!DOCTYPE html>
<html lang="en">
<head>
<meta charset="utf-8">
<title>Velvet Crest Coffee – Bag Print</title>
<link rel="stylesheet" href="https://fonts.googleapis.com/css2?family=Cinzel:wght@400;500&family=Tinos&display=swap">
<style>
  :root {
    --bag-black: #000000;
    --gold: #efe4a2;
    --gold-soft: #d8c77e;
    --cream: #f6efc4;
    --bean-dark: #2a140a;
    --bean-mid: #5a3018;
    --bean-light: #7c4625;
  }
  html, body {
    margin: 0;
    padding: 0;
    overflow: hidden;
    background: var(--bag-black);
  }
  .bag-print {
    position: relative;
    width: 1200px;
    height: 636px;
    background: var(--bag-black);
    overflow: hidden;
  }
  .brand-block {
    position: absolute;
    left: 110px;
    top: 48px;
    width: 1000px;
    height: 220px;
    transform: rotate(-9deg);
    transform-origin: center;
  }
  .brand-title {
    position: absolute;
    left: 40px;
    top: 20px;
    margin: 0;
    font-family: "Cinzel", serif;
    font-weight: 500;
    font-size: 64px;
    letter-spacing: 1px;
    color: var(--gold);
    white-space: nowrap;
  }
  .brand-subtitle {
    position: absolute;
    left: 270px;
    top: 102px;
    margin: 0;
    font-family: "Cinzel", serif;
    font-weight: 400;
    font-size: 38px;
    color: var(--gold);
    white-space: nowrap;
  }
  .flourish {
    position: absolute;
    height: 22px;
    border-radius: 11px;
    background: linear-gradient(90deg, rgba(239,228,162,0), rgba(239,228,162,0.55), rgba(239,228,162,0));
  }
  .flourish--left { left: 20px; top: 130px; width: 220px; }
  .flourish--right { left: 800px; top: 118px; width: 160px; }
  .company {
    position: absolute;
    left: 20px;
    top: 352px;
    width: 330px;
    text-align: center;
    font-family: "Tinos", "Times New Roman", serif;
    font-size: 26px;
    line-height: 1.45;
    color: var(--gold);
  }
  .company p { margin: 0; }
  .contents-box {
    position: absolute;
    left: 27px;
    top: 447px;
    width: 325px;
    height: 156px;
    box-sizing: border-box;
    border: 3px double var(--cream);
    outline: 1px solid var(--cream);
    outline-offset: 4px;
    display: flex;
    align-items: center;
    justify-content: center;
  }
  .contents-text {
    margin: 0;
    font-family: "Tinos", "Times New Roman", serif;
    font-size: 19.5px;
    line-height: 1.22;
    text-align: center;
    color: var(--cream);
  }
  .bean-pile {
    position: absolute;
    left: 0;
    top: 0;
  }
</style>
</head>
<body>
<main class="bag-print">
  <svg class="bean-pile" width="1200" height="636" viewBox="0 0 1200 636" role="img" aria-label="Photograph of a heap of roasted coffee beans">
    <defs>
      <radialGradient id="beanGlow" cx="0.6" cy="0.55" r="0.7">
        <stop offset="0" stop-color="var(--bean-light)"/>
        <stop offset="0.55" stop-color="var(--bean-mid)"/>
        <stop offset="1" stop-color="var(--bean-dark)"/>
      </radialGradient>
    </defs>
    <path d="M385 636 C420 560 480 500 560 470 C620 440 680 405 760 385 C820 372 880 378 940 395 C1010 405 1080 430 1140 470 C1175 495 1195 520 1200 540 L1200 636 Z" fill="url(#beanGlow)"/>
  </svg>

  <div class="brand-block">
    <h1 class="brand-title">Velvet Crest Coffee</h1>
    <p class="brand-subtitle">100% Arabica Coffee</p>
    <div class="flourish flourish--left" role="img" aria-label="Decorative gold flourish"></div>
    <div class="flourish flourish--right" role="img" aria-label="Decorative gold flourish"></div>
  </div>

  <div class="company">
    <p>Corvane &amp; Reed Coffee</p>
    <p>Brenhollow, TX 75811</p>
  </div>

  <div class="contents-box">
    <p class="contents-text">This package contains<br>one filter pack coffee and<br>may also contain sugar,<br>non-dairy creamer,<br>sugar sub., and stirrer.</p>
  </div>
</main>
</body>
</html>
```